Sign Front of Business

Sign for front of workshop. We want Tolvar Mechanical in same font and colour as logo then the logo after name. Would like a background colour maybe dark blue with a border.

Target Market(s)

Mining Community

Industry/Entity Type

Mechanical

Requirements
Must have
• Logo colours

```html
<!DOCTYPE html>
<html lang="en">
<head>
<meta charset="utf-8">
<title>Tolvar Mechanical – Workshop Sign</title>
<link href="https://fonts.googleapis.com/css2?family=Michroma&display=swap" rel="stylesheet">
<style>
  :root {
    --page-bg: #d9dbde;
    --frame-white: #f4f5f6;
    --sign-blue: #0f5bd0;
    --sign-blue-dark: #0b49b3;
    --sign-blue-light: #2a6fe0;
    --silver-light: #ffffff;
    --silver-mid: #d5d8dc;
    --silver-dark: #9aa0a8;
    --text-shadow: #073a8f;
    --mark-white: #ffffff;
  }
  * { margin: 0; padding: 0; box-sizing: border-box; }
  html, body {
    width: 1200px;
    height: 1000px;
    overflow: hidden;
    background: var(--page-bg);
  }
  .canvas {
    width: 1200px;
    height: 1000px;
    display: flex;
    align-items: center;
    justify-content: center;
  }
  .sign {
    width: 1120px;
    height: 170px;
    background: var(--frame-white);
    padding: 9px;
    box-shadow: 0 10px 24px rgba(0, 0, 0, 0.25);
  }
  .sign-panel {
    position: relative;
    width: 100%;
    height: 100%;
    background:
      linear-gradient(120deg, transparent 0 18%, rgba(255,255,255,0.06) 18% 34%, transparent 34% 52%, rgba(0,0,0,0.07) 52% 66%, transparent 66% 80%, rgba(255,255,255,0.05) 80% 100%),
      linear-gradient(90deg, var(--sign-blue-light), var(--sign-blue) 45%, var(--sign-blue-dark));
    display: flex;
    align-items: center;
    overflow: hidden;
  }
  .business-name {
    margin-left: 36px;
    display: flex;
    align-items: baseline;
    gap: 22px;
    font-family: "Michroma", sans-serif;
    text-transform: uppercase;
    white-space: nowrap;
  }
  .business-name span {
    background: linear-gradient(180deg, var(--silver-light) 0%, var(--silver-mid) 55%, var(--silver-dark) 100%);
    -webkit-background-clip: text;
    background-clip: text;
    color: transparent;
    filter: drop-shadow(3px 3px 0 var(--text-shadow));
  }
  .name-primary {
    font-size: 54px;
    letter-spacing: -1px;
  }
  .name-secondary {
    font-size: 38px;
    letter-spacing: 0;
  }
  .brand-mark {
    position: absolute;
    right: 48px;
    top: 50%;
    transform: translateY(-50%);
    display: flex;
    align-items: center;
    gap: 14px;
  }
  .brand-mark-dot {
    width: 46px;
    height: 46px;
    border-radius: 50%;
    background: var(--mark-white);
  }
  .brand-mark-name {
    font-family: "Michroma", sans-serif;
    font-size: 40px;
    color: var(--mark-white);
  }
</style>
</head>
<body>
  <main class="canvas">
    <div class="sign">
      <div class="sign-panel">
        <h1 class="business-name">
          <span class="name-primary">Tolvar</span>
          <span class="name-secondary">Mechanical</span>
        </h1>
        <div class="brand-mark">
          <div class="brand-mark-dot"></div>
          <div class="brand-mark-name">KRT</div>
        </div>
      </div>
    </div>
  </main>
</body>
</html>
```